Zielgruppe
Wir produzieren Rebuilt Toner Kartuschen und vertreiben diese an privat Anwender und auch Firmen Kunden.
Unsere Produkte vertreiben wir unter einer eigenen Marke und auch neutral an Wiederverkäufer.
Jetzt suchen wir ein neues Produkt Aufkleber Design für die neutrale Ware (ohne Logo) soll aber trotzdem ein Wiedererkennungswert haben, aber nicht direkt auf uns zurückführen.
Ein Bild vom aktuellen Aufkleber, ist anbei.
Aufgabenstellung
Es soll ein universal Design sein welches wir für alle Produkte verwenden können. Somit keine Artikel Informationen im Design.
Als Text soll 'Rebuilt Cartridge' und 'Made in Germany' verwendet werden.
Das Design soll die hohe Qualität unterstreichen.
Die Hintergrundfarbe soll Schwarz sein.
Der Standard Aufkleber soll die Abmessungen 233x84mm haben.

```html
<!DOCTYPE html>
<html lang="de">
<head>
<meta charset="utf-8">
<title>Rebuilt Cartridge – Etikett</title>
<link rel="stylesheet" href="https://fonts.googleapis.com/css2?family=Bodoni+Moda:wght@400;500&display=swap">
<style>
  :root {
    --page-bg: #f4f4f2;
    --label-black: #0b0b0c;
    --carbon-dark: #121213;
    --carbon-light: #1e1e20;
    --white: #ffffff;
    --gold-serif: #ecd88a;
  }

  * { margin: 0; padding: 0; box-sizing: border-box; }

  html, body {
    width: 1200px;
    height: 690px;
    overflow: hidden;
    background: var(--page-bg);
  }

  .canvas {
    width: 1200px;
    height: 690px;
    display: flex;
    align-items: center;
    justify-content: center;
  }

  .label {
    position: relative;
    width: 1100px;
    height: 397px;
    background: var(--label-black);
    overflow: hidden;
  }

  .label-texture {
    position: absolute;
    inset: 0;
    background: radial-gradient(ellipse at 50% 50%, var(--carbon-light) 0%, var(--carbon-dark) 60%, var(--label-black) 100%);
  }

  .label-copy {
    position: absolute;
    inset: 0;
    display: flex;
    flex-direction: column;
    align-items: center;
    justify-content: center;
    gap: 14px;
  }

  .tagline-premium {
    font-family: "Bodoni Moda", serif;
    font-weight: 400;
    font-size: 38px;
    letter-spacing: 0.55em;
    margin-right: -0.55em;
    color: var(--gold-serif);
    line-height: 1;
  }

  .product-title {
    font-family: "Bodoni Moda", serif;
    font-weight: 500;
    font-size: 76px;
    line-height: 1.1;
    letter-spacing: 0.04em;
    color: var(--white);
    white-space: nowrap;
  }

  .tagline-origin {
    font-family: "Bodoni Moda", serif;
    font-weight: 400;
    font-size: 34px;
    letter-spacing: 0.28em;
    margin-right: -0.28em;
    color: var(--gold-serif);
    line-height: 1;
  }
</style>
</head>
<body>
  <main class="canvas">
    <section class="label">
      <div class="label-texture" role="img" aria-label="Schwarzer Carbon-Hintergrund mit dunklen Sechseck-Elementen in den Ecken"></div>
      <div class="label-copy">
        <p class="tagline-premium">PREMIUM</p>
        <h1 class="product-title">REBUILT CARTRIDGE</h1>
        <p class="tagline-origin">MADE IN GERMANY</p>
      </div>
    </section>
  </main>
</body>
</html>
```